Business Card Design Project

Business Card
We are rebranding with a new logo
Industry/Entity Type
Business
Contact Information for Business Card
Dennis Marlow +61 427581962 dennis@qovo.com.au P.O. Box 872 Kelvindale QLD 4309
Requirements
Must have
- Logo

```html
<!DOCTYPE html>
<html lang="en">
<head>
<meta charset="utf-8">
<title>Qovo International – Business Card</title>
<link rel="stylesheet" href="https://fonts.googleapis.com/css2?family=Source+Sans+3:wght@400;600;700&display=swap">
<style>
  :root {
    --backdrop: #33221a;
    --card-white: #ffffff;
    --blue-light: #0a9ad6;
    --blue-deep: #0569a8;
    --orange-light: #f8a532;
    --orange-deep: #ee5a24;
    --name-yellow: #f1ea3b;
    --text-white: #ffffff;
    --brand-blue: #0a7fc2;
  }
  * { margin: 0; padding: 0; box-sizing: border-box; }
  html, body {
    width: 1200px;
    height: 848px;
    overflow: hidden;
    background: var(--backdrop);
    font-family: "Source Sans 3", sans-serif;
  }
  .card {
    position: absolute;
    left: 120px;
    top: 152px;
    width: 960px;
    height: 544px;
    border-radius: 22px;
    overflow: hidden;
  }
  .card-surface { position: absolute; inset: 0; display: block; }
  .brand {
    position: absolute;
    left: 60px;
    top: 228px;
    width: 310px;
    text-align: center;
    color: var(--brand-blue);
    font-weight: 700;
    line-height: 1;
  }
  .brand-name { display: block; font-size: 84px; letter-spacing: 1px; }
  .brand-division { display: block; font-size: 30px; letter-spacing: 3px; margin-top: 8px; }
  .holder-name {
    position: absolute;
    left: 552px;
    top: 124px;
    color: var(--name-yellow);
    font-size: 41px;
    font-weight: 700;
    line-height: 1;
  }
  .contact-list {
    position: absolute;
    left: 566px;
    top: 240px;
    list-style: none;
    color: var(--text-white);
    font-size: 31px;
    line-height: 38px;
  }
  .contact-item {
    display: flex;
    align-items: flex-start;
    margin-bottom: 14px;
  }
  .contact-icon {
    width: 28px;
    height: 38px;
    margin-right: 10px;
    flex: none;
    display: flex;
    align-items: center;
    justify-content: center;
    color: var(--orange-light);
    font-weight: 700;
  }
</style>
</head>
<body>
  <section class="card" aria-label="Qovo International business card for Dennis Marlow">
    <svg class="card-surface" viewBox="0 0 960 544" aria-hidden="true">
      <defs>
        <linearGradient id="panel-blue" x1="0" y1="0" x2="1" y2="1">
          <stop offset="0" stop-color="var(--blue-light)"/>
          <stop offset="1" stop-color="var(--blue-deep)"/>
        </linearGradient>
      </defs>
      <rect width="960" height="544" fill="var(--card-white)"/>
      <path d="M345 0 Q470 250 415 544 L960 544 L960 0 Z" fill="var(--orange-light)"/>
      <path d="M375 0 Q490 260 432 544 L960 544 L960 0 Z" fill="var(--orange-deep)"/>
      <path d="M402 0 Q510 270 450 544 L960 544 L960 0 Z" fill="url(#panel-blue)"/>
    </svg>

    <div class="brand">
      <span class="brand-name">Qovo</span>
      <span class="brand-division">INTERNATIONAL</span>
    </div>

    <h1 class="holder-name">Dennis Marlow</h1>

    <ul class="contact-list">
      <li class="contact-item">
        <span class="contact-icon">
          <svg width="18" height="28" viewBox="0 0 18 28" aria-hidden="true">
            <rect x="1.5" y="1.5" width="15" height="25" rx="3" fill="none" stroke="var(--orange-light)" stroke-width="3"/>
            <rect x="5" y="5" width="8" height="13" fill="var(--orange-light)"/>
          </svg>
        </span>
        <span>+61 427581962</span>
      </li>
      <li class="contact-item">
        <span class="contact-icon">@</span>
        <span>dennis@qovo.com.au</span>
      </li>
      <li class="contact-item">
        <span class="contact-icon">
          <svg width="28" height="20" viewBox="0 0 28 20" aria-hidden="true">
            <rect x="0" y="0" width="28" height="20" fill="var(--orange-light)"/>
            <path d="M1 1 L14 12 L27 1" fill="none" stroke="var(--blue-deep)" stroke-width="2"/>
          </svg>
        </span>
        <span>P.O. Box 872<br>Kelvindale QLD 4309</span>
      </li>
    </ul>
  </section>
</body>
</html>
```